PerkParcel.com.au Web Redesign

We need a web redesign for our existing website at http://perkparcel.com.au. Our website hosts a registration form for users who are interested in surveys, samples/trials, competitions (contests), and freebie offers. We rely heavily on emails as our main tool to communicate with our users. The current theme of our website is really white and bright. We would like to see a rather bold but playful theme like red, orange, and dark grey. The final design should be able to: 1) entice users to register; 2) look fun & playful; 3) have the modern, but colorful touch; and 4) present the theme of the offers (i.e. Brims, Lark/Plumfields, and Marlow Finch gift cards). The current logo can be redesigned into a new logo to suit the new web design.
Updates

Your new design must cover the following pages:

/index.html
/catalogue.html
/confirm-your-subscription.html
/contact-us.html
/daily-deals.html
/faqs.html
/terms-of-use.html
/thank-you.html

I missed out two extra pages that should be included in this project

/restaurant.html
/travel.html

Project Deadline Extended
Reason: Deadline is now extended by 15 more days. This should give you more time to be creative.

Target Market(s)

Age 18-65, both males & females, any occupations.

Requirements
Must have
• The new design must have the corresponding theme of the offer presented (Brims, LARK/Plumfields, and Marlow Finch).
Nice to have
• The current layout of our website crams all 3 gift card offers into one page. Feel free to redesign the website into 3 different pages with each page containing a dedicated offer. This will enhance the theme of the offer presented.

```html
<!DOCTYPE html>
<html lang="en">
<head>
<meta charset="utf-8">
<title>PerkParcel – Register</title>
<link rel="stylesheet" href="https://fonts.googleapis.com/css2?family=Raleway:wght@400;500;600&family=Roboto+Condensed:wght@700&family=Ubuntu:wght@400;500;700&family=Fredoka:wght@600&display=swap">
<style>
:root{
  --navy:#0b1729;
  --orange:#f07f00;
  --orange-dark:#d76a00;
  --green:#7cc412;
  --green-dark:#5fa50a;
  --charcoal:#3c3c3c;
  --slate:#3e3e3e;
  --text:#555;
  --muted:#777;
  --line:#d6d6d6;
  --panel:#f7f7f7;
  --footer:#454545;
  --white:#fff;
}
*{box-sizing:border-box;margin:0;padding:0}
html,body{width:1042px;height:1200px;overflow:hidden}
body{position:relative;background:#fff;font-family:"Raleway",sans-serif;color:var(--text)}
.abs{position:absolute}

/* header */
.site-header{left:0;top:0;width:1042px;height:96px;background:var(--navy)}
.brand{left:104px;top:24px;font-family:"Ubuntu",sans-serif;font-weight:700;font-size:35px;line-height:40px;color:var(--white);letter-spacing:-.5px}
.tagline{left:104px;top:70px;font-size:11.5px;color:#dfe4ea;font-weight:500}
.main-nav a{position:absolute;top:50px;font-size:11.5px;line-height:14px;color:var(--white);text-decoration:none;font-weight:500;white-space:nowrap}
.main-nav .active{left:484px;top:46px;width:90px;height:23px;line-height:23px;text-align:center;border-radius:3px;background:linear-gradient(#8fd31c,#5fa50a);color:#1d3a00}

/* hero */
.hero{left:0;top:96px;width:1042px;height:555px;background:linear-gradient(180deg,#1f63c8 0%,#4d94e4 28%,#a6cdf0 55%,#6eaa2c 57%,#4e9a1b 75%,#3f8a16 100%)}
.register-card{left:88px;top:175px;width:368px;height:242px;border-radius:8px;background:rgba(255,255,255,.32);border:1px solid rgba(255,255,255,.5)}
.register-title{left:103px;top:180px;font-family:"Fredoka",sans-serif;font-size:46px;line-height:56px;color:var(--green);text-shadow:0 2px 0 #fff,0 0 4px #fff}
.register-sub{left:106px;top:250px;width:340px;font-size:20px;line-height:23px;color:#1d2433;font-weight:500;letter-spacing:.4px}
.register-win{left:107px;top:344px;width:340px;font-family:"Roboto Condensed",sans-serif;font-size:27px;line-height:31px;color:#1d2433;letter-spacing:.3px}

.device{left:483px;top:156px;width:447px;height:438px;border-radius:20px;background:#111;border:2px solid #333}
.device-brand{left:483px;top:160px;width:447px;text-align:center;font-family:"Ubuntu",sans-serif;font-weight:700;font-size:21px;color:var(--white)}
.signup-form{left:523px;top:192px;width:370px;height:364px;background:var(--white)}
.field{position:absolute;left:0;width:370px;height:19px}
.field label{position:absolute;right:267px;top:3px;font:bold 10px Arial,sans-serif;color:#333;white-space:nowrap}
.field .input{position:absolute;left:121px;width:222px;height:19px;background:#efefef;border:1px solid #dcdcdc;font:10px Arial,sans-serif;color:#888;padding:3px 5px;white-space:nowrap}
.field .select::after{content:"";position:absolute;right:2px;top:2px;width:13px;height:13px;background:#fff;border:1px solid #888}
.field .select::before{content:"";position:absolute;right:6px;top:7px;border:3px solid transparent;border-top:4px solid #222;z-index:1}
.consent{position:absolute;left:16px;top:294px;font:9px Arial,sans-serif;color:#333;display:flex;align-items:center;gap:6px;white-space:nowrap}
.consent span{width:11px;height:11px;border:1px solid #999;background:#f4f4f4}
.submit{position:absolute;left:221px;top:320px;width:122px;height:33px;border-radius:17px;background:linear-gradient(#f9a12b,var(--orange-dark));border:2px solid #fbd39c;color:#fff;font-family:"Roboto Condensed",sans-serif;font-size:22px;text-align:center;line-height:29px}

/* content */
.content-band{left:0;top:651px;width:1042px;height:508px;background:linear-gradient(#e8e8e8,#fff 120px)}
.card{background:var(--panel);border:1px solid #e4e4e4;border-radius:6px;box-shadow:0 1px 2px rgba(0,0,0,.05)}
.why{left:105px;top:686px;width:247px;height:261px}
.why h2{position:absolute;left:13px;top:9px;font-family:"Ubuntu",sans-serif;font-weight:700;font-size:22px;color:var(--charcoal)}
.why h2 em,.lead h2 em{font-style:normal;color:var(--orange)}
.why ul{position:absolute;left:13px;top:38px;width:215px;list-style:none}
.why li{height:31.3px;border-bottom:1px dashed var(--line);font-size:11.5px;color:#444;padding-top:8px;padding-left:13px;position:relative}
.why li:last-child{border:none}
.why li::before{content:"";position:absolute;left:1px;top:14px;width:4px;height:4px;border-radius:50%;background:#333}
.lead{left:378px;top:686px;width:561px;height:261px}
.lead h2{position:absolute;left:13px;top:8px;font-family:"Ubuntu",sans-serif;font-weight:400;font-size:20px;color:var(--charcoal);white-space:nowrap}
.lead .divider{position:absolute;left:273px;top:52px;width:1px;height:176px;background:var(--line)}
.col{position:absolute;top:52px;width:232px}
.col h3{font-family:"Ubuntu",sans-serif;font-weight:400;font-size:15.5px;color:var(--green-dark);margin-bottom:9px}
.col p{font-size:11.3px;line-height:17.4px;color:var(--muted)}
.col .more{position:absolute;top:177px;font-size:10px;font-style:italic;color:#444}
.col-left{left:13px}
.col-right{left:302px;top:48px}
.col-right .more{top:179px}

/* offers */
.offers{left:105px;top:978px;width:837px;height:139px}
.offer-title{position:absolute;top:988px;font-family:"Ubuntu",sans-serif;font-weight:700;font-size:26px;line-height:28px;color:#fff;letter-spacing:.5px;white-space:nowrap}
.offer-list{position:absolute;list-style:none;font-size:11.5px;color:#fff;line-height:17.4px;white-space:nowrap}
.offer-list li::before{content:"•";margin-right:6px}
.gift{position:absolute;color:#fff;line-height:1;width:95px}
.gift b{display:block;font-weight:400;font-size:28px;text-align:right;padding-right:10px}
.gift span{display:block;font-size:21px}

/* footer */
.site-footer{left:0;top:1159px;width:1042px;height:41px;background:var(--footer);font-size:10.5px;color:#eee}
.site-footer .left{position:absolute;left:106px;top:15px}
.site-footer .right{position:absolute;right:100px;top:15px;word-spacing:2px}
</style>
</head>
<body>

<header class="site-header abs">
  <div class="brand abs">PerkParcel</div>
  <div class="tagline abs">Bringing Aussie's Best Rewards to You</div>
  <nav class="main-nav">
    <a class="active" href="#">Competitions</a>
    <a href="#" style="left:591px">Surveys</a>
    <a href="#" style="left:662px">Freebies</a>
    <a href="#" style="left:735px">FAQS</a>
    <a href="#" style="left:792px">About Us</a>
    <a href="#" style="left:869px">Terms of Use</a>
  </nav>
</header>

<section class="hero abs" role="img" aria-label="Photo of blue sky with clouds over a green grass field, hands holding a tablet"></section>

<div class="register-card abs"></div>
<div class="register-title abs">Register Here!</div>
<p class="register-sub abs">Subsribe now for your chance to win our monthly rewards!</p>
<p class="register-win abs">Win a $500 Gift Card of Your Choice Every Month!</p>

<div class="device abs"></div>
<div class="device-brand abs">PerkParcel</div>
<form class="signup-form abs">
  <div class="field" style="top:23px"><label>First Name:</label><div class="input"></div></div>
  <div class="field" style="top:53px"><label>Last Name:</label><div class="input"></div></div>
  <div class="field" style="top:82px"><label>E-mail:</label><div class="input"></div></div>
  <div class="field" style="top:112px"><label>Gender:</label><div class="input select">Male</div></div>
  <div class="field" style="top:141px"><label>Year of Birth:</label><div class="input select">Select One</div></div>
  <div class="field" style="top:171px"><label>Suburb:</label><div class="input"></div></div>
  <div class="field" style="top:200px"><label>Post Code:</label><div class="input"></div></div>
  <div class="field" style="top:229px"><label>State:</label><div class="input select">Australian Capital Territory</div></div>
  <div class="field" style="top:259px"><label>Select your Prize:</label><div class="input select" style="left:124px">Australian Capital Territory</div></div>
  <div class="consent"><span></span>By ticking this box, you agree to subscribe to our newsletter &amp; accept</div>
  <div class="submit">Sumbit</div>
</form>

<div class="content-band abs"></div>

<aside class="why card abs">
  <h2>Why <em>Subscribe?</em></h2>
  <ul>
    <li>Free Registration</li>
    <li>Greater Chance to Win</li>
    <li>Privacy Protection</li>
    <li>Monthly Winning Draw</li>
    <li>No Credit Card Required</li>
    <li>Exclusive Online Offers</li>
    <li>Easy to Unsubscribe</li>
  </ul>
</aside>

<section class="lead card abs">
  <h2>Australia's Leading Source of <em>Online Competions &amp; Surveys</em></h2>
  <div class="col col-left">
    <h3>Rewarding Offer Only</h3>
    <p>At PerkParcel, we bring you the most popular competitions, surveys, freebies, and various samples and trials so that you can maximize your chance to be rewarded. Simply sign up with us and enter the chance to win our monthly $500 gift cards of your choice. This is just the beginning of the most rewarding experience...</p>
    <span class="more">More Details &raquo;</span>
  </div>
  <div class="divider"></div>
  <div class="col col-right">
    <h3>It is always Free!</h3>
    <p>By signing up, you will receive our weekly exclusive offers which are available to our members only. Registration is 100% free! You pay no fees, no subscriptions, no credit cards, and no hassles from telemarketers. We present you with the offers in your e-mail, you simply choose the ones that interest you.</p>
    <span class="more">More Details &raquo;</span>
  </div>
</section>

<svg class="offers abs" viewBox="121 1127 964 160" width="837" height="139" aria-hidden="true">
  <path d="M715,1127 L1005,1127 L1085,1207 L1005,1287 L715,1287 Z" fill="#7cc412"/>
  <path d="M420,1127 L717,1127 L797,1207 L717,1287 L420,1287 Z" fill="#fff"/>
  <path d="M420,1127 L705,1127 L785,1207 L705,1287 L420,1287 Z" fill="#3e3e3e"/>
  <path d="M128,1127 L437,1127 L517,1207 L437,1287 L128,1287 Z" fill="#fff"/>
  <path d="M131,1127 L425,1127 L505,1207 L425,1287 L131,1287 Q121,1287 121,1277 L121,1137 Q121,1127 131,1127 Z" fill="#f07f00"/>
  <path d="M361,1173 L470,1173 L490,1206 L470,1240 L361,1240 Z" fill="#fff" opacity=".2"/>
  <path d="M654,1173 L760,1173 L780,1206 L760,1240 L654,1240 Z" fill="#fff" opacity=".18"/>
  <path d="M951,1173 L1060,1173 L1078,1206 L1060,1240 L951,1240 Z" fill="#fff" opacity=".2"/>
</svg>

<div class="offer-title" style="left:122px">BRIMS &amp; HALDEN</div>
<ul class="offer-list" style="left:126px;top:1028px"><li>Free Registration</li><li>Greater Chance to Win</li><li>Privacy Protection</li><li>Monthly Winning Draw</li></ul>
<div class="gift" style="left:315px;top:1023px"><b>500</b><span>gift card</span></div>

<div class="offer-title" style="left:444px">LARK</div>
<ul class="offer-list" style="left:447px;top:1022px"><li>Free Registration</li><li>Greater&nbsp; to Win</li><li>Privacy Protection</li><li>Monthly Draw</li></ul>
<div class="gift" style="left:569px;top:1022px"><b>500</b><span>gift card</span></div>

<div class="offer-title" style="left:693px">MARLOW FINCH</div>
<ul class="offer-list" style="left:703px;top:1022px"><li>Free Registration</li><li>Greater to Win</li><li>Privacy Protection</li><li>Monthly Draw</li></ul>
<div class="gift" style="left:826px;top:1024px"><b>500</b><span>gift card</span></div>

<footer class="site-footer abs">
  <div class="left">PERKPARCEL © 2010 &nbsp;PRIVACY POLICY</div>
  <div class="right">FAQS &nbsp;| &nbsp;ABOUT US &nbsp;| &nbsp;CONTACT US &nbsp;| &nbsp;TERMS OF USE</div>
</footer>

</body>
</html>
```